Business Cards and Logo needed for Rum Website

I need a smart, modern but fun business card (and Logo) to help promote my website BrightBarrelNotes.com

The website contains reviews of Rum (and eventually other spirits) as well as news and blog posts.

I would like a 2-sided design, with the logo and company name on one side and text on the other.

Text fields required are:
Name (Dan Fowler)
Website (www.brightbarrelnotes.com)
Email (dan@brightbarrelnotes.com)
Twitter (@BrightBarrelNotes)

For the logo i'm open to suggestions however it must incorporate a wooden Cask and a number of Stars. Ideas so far have been for a Cask surrounded in a number of Stars forming a circle around it with the text Bright Barrel Notes underneath. The logo should be modern but also a little bit cartoony and stylised. General drink/spirits themes will also be considered.

Colours: I like the idea of yellow text with black background but again i'm open to suggestions on what would work well. Contrasting colours for the 2-sides would be good.

Cards will be printed via Pelv.com so please consult their style guidelines if required: http://uk.pelv.com/help/faq/templates-and-guidelines.html

Requirements
Must have
• A spirits Cask
A number of Stars (preferrably yellow or gold)

```html
<!DOCTYPE html>
<html lang="en">
<head>
<meta charset="utf-8">
<title>Bright Barrel Notes — Business Card</title>
<link href="https://fonts.googleapis.com/css2?family=Jost:wght@400&display=swap" rel="stylesheet">
<style>
  :root {
    --stage: #000000;
    --wood-dark-1: #7a7164;
    --wood-dark-2: #5e564b;
    --wood-dark-3: #6d6457;
    --wood-light-1: #e6e1d1;
    --wood-light-2: #cfc8b3;
    --wood-light-3: #ddd7c4;
    --seal: rgba(38, 24, 10, 0.62);
    --seal-edge: rgba(30, 18, 6, 0.75);
    --star-yellow: #eeec6c;
    --ink-brown: #4a2c14;
  }
  * { margin: 0; padding: 0; box-sizing: border-box; }
  html, body {
    width: 1200px;
    height: 900px;
    overflow: hidden;
    background: var(--stage);
  }
  .canvas {
    position: relative;
    width: 1200px;
    height: 900px;
    background: var(--stage);
    font-family: "Jost", "Futura", sans-serif;
  }
  .card {
    position: absolute;
    left: 300px;
    width: 600px;
    height: 342px;
    overflow: hidden;
  }
  .card--front { top: 72px; }
  .card--back { top: 487px; }
  .wood {
    position: absolute;
    inset: 0;
  }
  .wood--dark {
    background: linear-gradient(180deg,
      var(--wood-dark-1) 0%, var(--wood-dark-3) 35%,
      var(--wood-dark-2) 60%, var(--wood-dark-1) 100%);
  }
  .wood--light {
    background: linear-gradient(180deg,
      var(--wood-light-1) 0%, var(--wood-light-3) 40%,
      var(--wood-light-2) 70%, var(--wood-light-1) 100%);
  }
  .brand-seal {
    position: absolute;
    border-radius: 50%;
    background: var(--seal);
    border: 3px solid var(--seal-edge);
    display: flex;
    align-items: center;
    justify-content: center;
    text-align: center;
  }
  .card--front .brand-seal {
    left: 28px;
    top: 49px;
    width: 256px;
    height: 256px;
  }
  .card--back .brand-seal {
    left: 8px;
    top: 8px;
    width: 136px;
    height: 136px;
  }
  .brand-name {
    color: var(--star-yellow);
    font-weight: 400;
    letter-spacing: 1px;
    line-height: 1.15;
  }
  .card--front .brand-name { font-size: 26px; width: 180px; }
  .card--back .brand-name { font-size: 14px; width: 100px; }
  .contact {
    position: absolute;
    right: 22px;
    top: 208px;
    list-style: none;
    text-align: right;
    color: var(--ink-brown);
    font-size: 21px;
    letter-spacing: 2.2px;
    line-height: 31px;
    font-weight: 400;
  }
</style>
</head>
<body>
<main class="canvas">
  <section class="card card--front" aria-label="Card front">
    <div class="wood wood--dark" role="img" aria-label="Weathered grey wooden deck planks"></div>
    <div class="brand-seal">
      <span class="brand-name">Bright Barrel Notes</span>
    </div>
  </section>

  <section class="card card--back" aria-label="Card back">
    <div class="wood wood--light" role="img" aria-label="Pale cracked wooden planks"></div>
    <div class="brand-seal">
      <span class="brand-name">Bright Barrel Notes</span>
    </div>
    <ul class="contact">
      <li>Name: Dan Fowler</li>
      <li>Website: www.brightbarrelnotes.com</li>
      <li>Email: dan@brightbarrelnotes.com</li>
      <li>Twitter: @BrightBarrelNotes</li>
    </ul>
  </section>
</main>
</body>
</html>
```